Brindle Financial Advice - Employer Benefit Brochure

We need to design a professional looking brochure that we can present to our existing client base, and assist in attracting new clients.
The current information is just provided in a word document, but we need to improve significantly.
The audience would be business leaders, HR decision makers and member policy committee members

Industry/Entity Type

Business

Font styles to use
Sans Serif

Colors
0255a3
f37122

```html
<!DOCTYPE html>
<html lang="en">
<head>
<meta charset="utf-8">
<title>Brindle Financial Advice – Employer Benefits Program</title>
<link href="https://fonts.googleapis.com/css2?family=Marcellus+SC&family=Source+Sans+3:wght@400;600&display=swap" rel="stylesheet">
<style>
  :root {
    --brand-blue: #0255a3;
    --brand-orange: #f37122;
    --ink: #3d3d3d;
    --table-grey: #555557;
    --page: #ffffff;
    --backdrop: #e6e6e6;
    --photo-a: #c9c2b8;
    --photo-b: #8c8f95;
  }
  * { box-sizing: border-box; margin: 0; padding: 0; }
  html, body { width: 1200px; height: 800px; overflow: hidden; }
  body {
    background: var(--backdrop);
    font-family: "Source Sans 3", Arial, sans-serif;
    color: var(--ink);
    position: relative;
  }
  .spread {
    position: absolute; left: 40px; top: 20px;
    width: 1120px; height: 760px;
    display: flex;
    box-shadow: 0 6px 24px rgba(0,0,0,.18);
  }
  .page { position: relative; width: 560px; height: 760px; background: var(--page); overflow: hidden; }
  .page--left { border-right: 1px solid #ddd; }

  .masthead { position: absolute; left: 0; right: 0; top: 22px; height: 44px; }
  .masthead__rule {
    position: absolute; left: 0; right: 0; top: 30px; height: 6px;
    background: linear-gradient(90deg, #013f7a, var(--brand-blue) 40%, #3d8fd6 50%, var(--brand-blue) 60%, #013f7a);
  }
  .brand {
    position: absolute; left: 50%; top: 0; transform: translateX(-50%);
    display: flex; align-items: center; gap: 6px;
    background: var(--page); padding: 6px 10px;
  }
  .brand__mark { width: 20px; height: 20px; background: var(--brand-blue); }
  .brand__name { font-size: 15px; font-weight: 600; color: var(--brand-blue); }

  .cover-photo {
    position: absolute; left: 20px; right: 0; top: 66px; height: 326px;
    background: linear-gradient(160deg, var(--photo-a), #d9d4cc 45%, var(--photo-b));
  }
  .cover-rule { position: absolute; left: 20px; right: 0; top: 396px; height: 2px; background: var(--brand-orange); }
  .cover-band { position: absolute; left: 0; right: 0; top: 402px; bottom: 0; background: var(--brand-orange); }
  .cover-title {
    position: absolute; left: 160px; top: 470px; width: 158px; height: 182px;
    background: var(--brand-blue); color: #fff;
    display: flex; align-items: center; justify-content: center; text-align: center;
    font-family: "Marcellus SC", Georgia, serif; font-size: 21px; line-height: 1.25;
  }

  .content { position: absolute; left: 24px; right: 34px; top: 108px; }
  .content__title {
    font-family: "Marcellus SC", Georgia, serif; font-weight: 400;
    color: var(--brand-orange); font-size: 19px; line-height: 1.2; margin-bottom: 18px;
  }
  .content p { font-size: 11.5px; line-height: 1.45; margin-bottom: 13px; }

  .services { width: 100%; border-collapse: collapse; margin-top: 4px; font-size: 10.5px; line-height: 1.3; }
  .services th, .services td { vertical-align: top; padding: 7px 8px; border-bottom: 1px solid #fff; }
  .services th { width: 118px; background: var(--brand-orange); color: #fff; font-weight: 400; text-align: left; }
  .services td { background: var(--table-grey); color: #f2f2f2; height: 40px; }
  .services tr:last-child th, .services tr:last-child td { height: 52px; border-bottom: 0; }
</style>
</head>
<body>
  <main class="spread">
    <section class="page page--left">
      <header class="masthead">
        <div class="masthead__rule"></div>
        <div class="brand"><span class="brand__mark"></span><span class="brand__name">Brindle</span></div>
      </header>
      <div class="cover-photo" role="img" aria-label="Photo of a worried couple on a sofa reviewing bills with a calculator"></div>
      <div class="cover-rule"></div>
      <div class="cover-band"></div>
      <h1 class="cover-title">Employer<br>Benefits<br>Program</h1>
    </section>

    <section class="page page--right">
      <header class="masthead">
        <div class="masthead__rule"></div>
        <div class="brand"><span class="brand__mark"></span><span class="brand__name">Brindle</span></div>
      </header>
      <article class="content">
        <h2 class="content__title">CORE:<br>Corporate Superannuation Services</h2>
        <p>Brindle’s core offer is the ongoing support of the group employer superannuation solution.</p>
        <p>Superannuation is a long-term investment so it’s crucial to have the right partner who will consistently deliver outstanding support to you and your employees. Brindle has an extensive knowledge of superannuation providers in the market and can ensure that you have the right solution for your long-term business requirements.</p>
        <p>We are able to take over the servicing of the current group plan, or assist in setting up a plan for companies new to the market.</p>
        <p>The program we deliver has two unique components. Firstly, services to assist employers in providing a ‘best of breed’ superannuation solution to employees and secondly, proactive advice to employees to ensure that they take control of their individual financial situation.</p>
        <p>Below is an overview of the services and support Brindle provides to employers:</p>
        <table class="services">
          <tr><th>Choosing your employer super plan</th><td>Whether you are self-directed, or seeking a full advice service, we can assist you in your selection of the most suitable provider for your employees long-term retirement needs.</td></tr>
          <tr><th>Setting up a new super plan</th><td>We facilitate the complete application process, induction presentations for employees, lost super searches and the setting up of the online clearing facility for all your superannuation payments.</td></tr>
          <tr><th>Managing and Reviewing your employer super plan</th><td>We work together to build and deliver your annual Client Service Plan. We manage the annual review process, provide access to all relevant information and answer all employer and employee queries, complaints and facilitate the ongoing plan administration.</td></tr>
          <tr><th>Policy Committee management</th><td>We establish and manage a Policy Committee where required or desired. Responsibilities include initiating all meetings, preparing reports, minutes and the presentation of legislative product and education updates.</td></tr>
          <tr><th>Keeping you up to date</th><td>We provide you with all relevant communications to ensure that you meet your responsibilities and obligations.</td></tr>
        </table>
      </article>
    </section>
  </main>
</body>
</html>
```